Window and GutterCleaning Flyer A5 size double sided.

We need a double sided A5 flyer. Side 1, is for window cleaning, side 2 is for gutter cleaning. Licensed by Borough of Halvern Council.
Phone number 0800 315 4720.
Business address 7 Tarnlow Brae, North Pellin Edinburgh EH14 3RW.
www.clearpane-vista-services.com
We use a LoftPro Gutter inspection Cam to view your gutters first to see if they need doing.
Window cleaning ; Professional window cleaning services, what we offer, water fed pole window cleaning able to reach windows up to 60 feet.
Conservatory cleaning.
Conservatory roof cleaning.
Fascias & Soffits cleaning.
Excellent Customer Service.
Target Market(s)
domestic houses
Industry/Entity Type
window cleaning
Look and feel
Each slider illustrates characteristics of the customer's brand and the style your logo design should communicate.

```html
<!DOCTYPE html>
<html lang="en">
<head>
<meta charset="utf-8">
<title>ClearPane Vista – Window and Gutter Cleaning Flyer</title>
<link href="https://fonts.googleapis.com/css2?family=Oswald:wght@400;500;600&family=Montserrat:wght@800&display=swap" rel="stylesheet">
<style>
:root{
  --navy:#23226a;
  --blue:#2f3c9e;
  --sky:#8fb3e8;
  --sky-pale:#a9c8f0;
  --ink-dark:#2e2e33;
  --white:#ffffff;
  --stage:#4a4a4e;
}
*{margin:0;padding:0;box-sizing:border-box}
html,body{width:1200px;height:800px;overflow:hidden}
body{background:var(--stage);font-family:'Oswald',sans-serif;position:relative}
.flyer{position:absolute;top:50px;width:495px;height:700px;background:var(--white);overflow:hidden;box-shadow:0 10px 30px rgba(0,0,0,.35)}
.flyer--gutter{left:70px}
.flyer--window{left:635px}
.abs{position:absolute}
.brand{font-family:'Oswald',sans-serif;font-weight:600;color:var(--navy);text-align:center;line-height:1;display:flex;align-items:center;gap:8px}
.brand__mark{width:14px;height:14px;background:var(--navy);flex:none}
.brand__name{font-size:28px}
.photo{position:absolute}
.tick{width:16px;height:16px;flex:none}
.ticks{list-style:none}
.ticks li{display:flex;align-items:flex-start;gap:10px}

/* Gutter side */
.g-hero-photo{left:0;top:0;width:212px;height:200px;background:linear-gradient(160deg,#f4f5f8,#dfe3ea 60%,#cfd4dc)}
.g-brand{left:0;top:0;width:212px;height:200px;justify-content:center}
.g-title{left:212px;top:0;width:283px;height:200px;background:var(--navy);border-bottom-left-radius:60px;text-align:right;padding:18px 18px 0 0;font-weight:600;line-height:1.02;text-transform:uppercase}
.g-title__accent{display:block;color:var(--sky);font-size:55px}
.g-title__main{display:block;color:var(--white);font-size:51px}
.g-inspect{left:0;top:200px;width:495px;height:190px;background:linear-gradient(110deg,#2b3a8f 0%,#3c56a8 45%,#5a79b8 75%,#8aa0c4 100%)}
.g-inspect__title{left:30px;top:212px;color:var(--white);font-size:27px;font-weight:500;white-space:nowrap}
.g-inspect__list{left:30px;top:258px;color:var(--white);font-size:17px;line-height:1.2}
.g-inspect__list li{margin-bottom:5px}
.g-device{left:300px;top:252px;width:150px;height:98px;border-radius:10px;background:linear-gradient(135deg,#1c1c22,#3b4250 40%,#6f8fb5 55%,#1c1c22 90%);transform:rotate(-6deg)}
.g-pill{left:142px;top:368px;width:211px;height:36px;border-radius:18px;background:var(--navy);color:var(--white);font-size:18px;font-weight:500;display:flex;align-items:center;justify-content:center;white-space:nowrap}
.g-card{position:absolute;top:459px;width:90px;height:125px;border:1.5px solid var(--navy);border-top:none;border-radius:0 0 12px 12px;color:var(--navy);text-align:center;font-size:13.5px;line-height:1.12;padding:45px 3px 0}
.g-circle{position:absolute;top:415px;width:88px;height:88px;border-radius:50%;border:4px solid var(--white);box-shadow:0 2px 6px rgba(0,0,0,.25)}
.g-why{left:16px;top:597px;width:459px;height:67px;background:var(--ink-dark);border-radius:30px 30px 0 0;color:var(--white)}
.g-why__head{position:absolute;left:16px;top:9px;font-size:16px;font-weight:500;white-space:nowrap}
.g-why__phone{position:absolute;right:16px;top:5px;display:flex;align-items:center;gap:7px;font-family:'Montserrat',sans-serif;font-weight:800;font-size:25px;white-space:nowrap}
.g-why__points{position:absolute;left:16px;top:42px;font-size:13px;white-space:nowrap}
.g-foot{left:0;top:664px;width:495px;height:36px;background:var(--navy);color:var(--white);font-size:14.5px;display:flex;align-items:center;justify-content:center;white-space:nowrap}

/* Window side */
.w-column{left:0;top:0;width:220px;height:630px;background:linear-gradient(170deg,#1f2a7a 0%,#2e45a6 35%,#4a6cc2 60%,#2a3790 100%);border-bottom-right-radius:80px}
.w-label{left:0;top:14px;width:220px;height:34px;background:var(--sky-pale);color:var(--navy);font-size:16px;font-weight:500;display:flex;align-items:center;justify-content:center;white-space:nowrap;letter-spacing:-.2px}
.w-service{position:absolute;left:27px;width:172px;height:64px;border:1.5px solid rgba(169,200,240,.8);border-right:none;border-radius:12px 0 0 12px;color:var(--white);font-size:13px;line-height:1.18;padding:0 28px 0 9px;display:flex;align-items:center}
.w-circle{position:absolute;left:177px;width:96px;height:96px;border-radius:50%;border:5px solid var(--white);box-shadow:0 2px 8px rgba(0,0,0,.3)}
.w-hero-photo{left:220px;top:0;width:275px;height:200px;background:linear-gradient(200deg,#f6f7fa,#e2e8f1 55%,#d3dbe8)}
.w-brand{left:220px;top:0;width:275px;height:200px;justify-content:center}
.w-title{left:220px;top:200px;width:275px;height:190px;background:var(--navy);text-align:right;padding:10px 28px 0 0;font-weight:600;font-size:55px;line-height:1.02;text-transform:uppercase;color:var(--white)}
.w-title__accent{color:var(--sky)}
.w-choose{left:280px;top:408px;width:190px;height:141px;border:2px solid var(--sky-pale);border-radius:12px;padding:8px 0 0 10px;color:var(--navy)}
.w-choose__head{font-size:23px;font-weight:500;margin-bottom:4px}
.w-choose .ticks{font-size:15.5px;line-height:1.2}
.w-choose .ticks li{margin-bottom:4px;gap:7px;white-space:nowrap}
.w-license{left:261px;top:557px;width:207px;height:23px;background:var(--navy);color:var(--white);font-size:13px;display:flex;align-items:center;justify-content:center;white-space:nowrap}
.w-phone{right:27px;top:588px;display:flex;align-items:center;gap:8px;font-family:'Montserrat',sans-serif;font-weight:800;font-size:28px;color:var(--navy);white-space:nowrap}
.w-address{left:0;top:632px;width:495px;text-align:center;font-size:14px;color:var(--navy);white-space:nowrap}
.w-band{left:0;top:666px;width:495px;height:34px;background:var(--sky-pale);color:var(--navy);font-family:'Montserrat',sans-serif;font-weight:800;font-size:14px;display:flex;align-items:center;justify-content:center;white-space:nowrap}
</style>
</head>
<body>
<svg width="0" height="0" style="position:absolute">
  <defs>
    <symbol id="tick-white" viewBox="0 0 16 16"><circle cx="8" cy="8" r="7.5" fill="#fff"/><path d="M4.3 8.2l2.4 2.5 5-5.6" fill="none" stroke="#2f3c9e" stroke-width="2.2" stroke-linecap="round" stroke-linejoin="round"/></symbol>
    <symbol id="tick-blue" viewBox="0 0 16 16"><circle cx="8" cy="8" r="7.5" fill="#2f3c9e"/><path d="M4.3 8.2l2.4 2.5 5-5.6" fill="none" stroke="#fff" stroke-width="2.2" stroke-linecap="round" stroke-linejoin="round"/></symbol>
    <symbol id="phone" viewBox="0 0 24 24"><circle cx="12" cy="12" r="10.5" fill="none" stroke="currentColor" stroke-width="2.4"/><path d="M8.6 6.8c.5-.4 1.1-.3 1.4.2l1 1.7c.2.4.1.9-.2 1.2l-.7.6c.5 1.2 1.4 2.2 2.5 2.8l.7-.6c.3-.3.8-.3 1.2-.1l1.7 1c.5.3.6.9.2 1.4l-.8 1c-.5.5-1.3.7-2 .4-2.8-1.1-5-3.4-6-6.2-.3-.7 0-1.5.5-2z" fill="currentColor"/></symbol>
  </defs>
</svg>

<!-- Side 2: gutter cleaning -->
<section class="flyer flyer--gutter">
  <div class="photo g-hero-photo" role="img" aria-label="Soft-focus photo of a white house front behind the company name"></div>
  <div class="abs brand g-brand"><span class="brand__mark"></span><span class="brand__name">ClearPane Vista</span></div>
  <h1 class="abs g-title"><span class="g-title__accent">Gutter</span><span class="g-title__main">Cleaning &amp;</span><span class="g-title__main">Inspection</span></h1>

  <div class="photo g-inspect" role="img" aria-label="Blue-toned photo of a house roof and gutter full of autumn leaves"></div>
  <h2 class="abs g-inspect__title">Gutter Inspections with LoftPro<sup style="font-size:11px">®</sup> Cam</h2>
  <ul class="abs ticks g-inspect__list">
    <li><svg class="tick"><use href="#tick-white"/></svg><span>We inspect first – no guesswork</span></li>
    <li><svg class="tick"><use href="#tick-white"/></svg><span>You only pay if cleaning is needed!</span></li>
    <li><svg class="tick"><use href="#tick-white"/></svg><span>Real-time footage using LoftPro<br>SightLine Inspection System</span></li>
  </ul>
  <div class="photo g-device" role="img" aria-label="Handheld inspection camera monitor showing a house on screen"></div>

  <div class="abs g-pill">GUTTER CLEANING SERVICES</div>

  <div class="g-card" style="left:21px">Safe from the ground with powerful vacuum system</div>
  <div class="g-card" style="left:141px">Removal of moss, leaves, and debris</div>
  <div class="g-card" style="left:263px">Ideal for conservatories, extensions, and hard-to-reach areas</div>
  <div class="g-card" style="left:386px">Prevent water damage and costly repairs</div>
  <div class="g-circle" role="img" aria-label="Vacuum hose clearing a gutter" style="left:22px;background:linear-gradient(150deg,#6a7ca8,#c9ccd2 55%,#8b8f95)"></div>
  <div class="g-circle" role="img" aria-label="Gutter clogged with leaves and moss" style="left:142px;background:linear-gradient(150deg,#7d766c,#a0784a 50%,#5c5448)"></div>
  <div class="g-circle" role="img" aria-label="White conservatory with glass roof" style="left:264px;background:linear-gradient(180deg,#cfe0f0,#f2f2f2 50%,#9c6a52)"></div>
  <div class="g-circle" role="img" aria-label="Couple at home looking at water damage on a ceiling" style="left:387px;background:linear-gradient(150deg,#6b5a4a,#b79a78 55%,#4d4038)"></div>

  <div class="abs g-why">
    <span class="g-why__head">Why Book Gutter Cleaning?</span>
    <span class="g-why__phone"><svg width="22" height="22"><use href="#phone"/></svg>0800 315 4720</span>
    <span class="g-why__points">Helps avoid roof leaks &nbsp;|&nbsp; Maintains property value &nbsp;|&nbsp; Recommended annually for all homes</span>
  </div>
  <footer class="abs g-foot">7 Tarnlow Brae, North Pellin, Edinburgh EH14 3RW &nbsp;|&nbsp; www.clearpane-vista-services.com</footer>
</section>

<!-- Side 1: window cleaning -->
<section class="flyer flyer--window">
  <div class="photo w-column" role="img" aria-label="Blue-toned photo of a window cleaner using a water-fed pole"></div>
  <div class="abs w-label">OUR PROFESSIONAL SERVICES</div>

  <div class="w-service" style="top:74px">Water-fed pole window cleaning reaches upto 60ft safely from the ground</div>
  <div class="w-service" style="top:178px">Conservatory glass &amp; roof cleaning</div>
  <div class="w-service" style="top:283px">Fascia and soffit cleaning</div>
  <div class="w-service" style="top:389px">Fully insured and reliable team</div>
  <div class="w-service" style="top:495px">Excellent customer service with flexible scheduling</div>
  <div class="w-circle" role="img" aria-label="Water-fed pole brush on a window" style="top:58px;background:linear-gradient(150deg,#8a4a3a,#e8ecf0 55%,#7c8696)"></div>
  <div class="w-circle" role="img" aria-label="Conservatory roof panels being cleaned" style="top:162px;background:linear-gradient(150deg,#9a6a56,#cfd6da 50%,#7e8a7a)"></div>
  <div class="w-circle" role="img" aria-label="Roofline showing gutter, fascia and soffit" style="top:267px;background:linear-gradient(150deg,#f2f2f2,#c7ccd3 50%,#7d5a4a)"></div>
  <div class="w-circle" role="img" aria-label="Two members of the cleaning team" style="top:373px;background:linear-gradient(150deg,#d9c9b5,#2a3a6a 55%,#c7d23a)"></div>
  <div class="w-circle" role="img" aria-label="Customer service advisor with headset" style="top:479px;background:linear-gradient(150deg,#e9eef4,#d6b89a 55%,#9fb3c8)"></div>

  <div class="photo w-hero-photo" role="img" aria-label="Soft-focus photo of clean glass windows behind the company name"></div>
  <div class="abs brand w-brand"><span class="brand__mark"></span><span class="brand__name">ClearPane Vista</span></div>
  <h1 class="abs w-title">Window<br><span class="w-title__accent">Cleaning</span><br>Services</h1>

  <div class="abs w-choose">
    <h2 class="w-choose__head">Why Choose Us?</h2>
    <ul class="ticks">
      <li><svg class="tick"><use href="#tick-blue"/></svg><span>Streak-free finish</span></li>
      <li><svg class="tick"><use href="#tick-blue"/></svg><span>No ladders, no mess</span></li>
      <li><svg class="tick"><use href="#tick-blue"/></svg><span>Affordable</span></li>
      <li><svg class="tick"><use href="#tick-blue"/></svg><span>Regular or one-off cleans</span></li>
    </ul>
  </div>
  <div class="abs w-license">Licensed by Borough of Halvern Council</div>
  <div class="abs w-phone"><svg width="24" height="24" style="color:var(--blue)"><use href="#phone"/></svg>0800 315 4720</div>
  <div class="abs w-address">7 Tarnlow Brae, North Pellin, Edinburgh EH14 3RW &nbsp;|&nbsp; www.clearpane-vista-services.com</div>
  <footer class="abs w-band">SERVING DOMESTIC HOMES THROUGHOUT EDINBURGH</footer>
</section>
</body>
</html>
```